Cold pressed organic juice company is expanding to do bone broths

I need 2 labels with the same look ,different colors one for beef bone broth , one for chicken bone broth, both with the addition of medicinal mushrooms. I would like the design to clearly indicate the inclusion of the mushrooms.
the labels with be applied to compostable brown container ( paper bag brown)
Container size is 5 1/2 inches tall(14cm )
Target Market(s)
Health conscious people
Requirements
Must have
- picture of medicinal mushroom along with logo provided, either color and this phrase added to the label : A blend of Ashwagandha and 8 medicinal mushrooms
Nice to have
- maybe some illustrations of medicinal mushrooms , maybe partial black and white ?
Should not have
- no animal pictures such as chickens or cows

```html
<!DOCTYPE html>
<html lang="en">
<head>
<meta charset="utf-8">
<title>Bone Broth Labels</title>
<link rel="stylesheet" href="https://fonts.googleapis.com/css2?family=Cinzel:wght@500&family=Dancing+Script:wght@600&family=Caveat:wght@500&display=swap">
<style>
  :root {
    --label-top: #ffffff;
    --label-mid: #e4e6e9;
    --wood-light: #e6d2b0;
    --wood-dark: #c9a87a;
    --chicken: #2f9e1e;
    --chicken-tab-top: #35c416;
    --chicken-tab-bottom: #1f8a1a;
    --beef: #e8473a;
    --beef-soft: #ef6a3c;
    --beef-tab-top: #f26a35;
    --beef-tab-bottom: #e53935;
    --ink-grey: #555a60;
    --on-tab: #ffffff;
  }
  * { box-sizing: border-box; margin: 0; padding: 0; }
  html, body { width: 1200px; height: 1000px; overflow: hidden; }
  body {
    background: linear-gradient(180deg, #cfcfcf 0%, #e6e6e6 100%);
    display: flex;
    align-items: center;
    justify-content: center;
    gap: 80px;
  }
  .label {
    position: relative;
    width: 460px;
    height: 760px;
    background: linear-gradient(180deg, var(--label-top) 0%, var(--label-mid) 62%);
    box-shadow: 0 10px 30px rgba(0,0,0,.12);
    display: flex;
    flex-direction: column;
    align-items: center;
    overflow: hidden;
  }
  .brand-tab {
    width: 180px;
    height: 220px;
    border-radius: 0 0 90px 90px;
    display: flex;
    flex-direction: column;
    align-items: center;
    justify-content: flex-end;
    padding-bottom: 52px;
    gap: 8px;
  }
  .label--chicken .brand-tab { background: linear-gradient(180deg, var(--chicken-tab-top), var(--chicken-tab-bottom)); }
  .label--beef .brand-tab { background: linear-gradient(180deg, var(--beef-tab-top), var(--beef-tab-bottom)); }
  .brand-dot {
    width: 16px; height: 16px; border-radius: 50%;
    background: var(--on-tab);
  }
  .brand-name {
    font-family: "Cinzel", serif;
    font-weight: 500;
    font-size: 18px;
    line-height: 1.15;
    color: var(--on-tab);
    text-align: center;
  }
  .brand-tagline {
    font-family: "Cinzel", serif;
    font-weight: 500;
    font-size: 8px;
    color: var(--on-tab);
    white-space: nowrap;
  }
  .flavour {
    font-family: "Dancing Script", cursive;
    font-weight: 600;
    font-size: 76px;
    line-height: 1;
    margin-top: 14px;
  }
  .product-line {
    display: flex;
    align-items: center;
    gap: 10px;
    font-family: "Cinzel", serif;
    font-weight: 500;
    font-size: 24px;
    letter-spacing: 1px;
    margin-top: 6px;
  }
  .product-line svg { display: block; }
  .blend-note {
    display: flex;
    align-items: flex-end;
    gap: 4px;
    margin-top: 12px;
    color: var(--ink-grey);
    font-family: "Caveat", cursive;
    font-weight: 500;
  }
  .blend-count {
    font-family: "Dancing Script", cursive;
    font-weight: 600;
    font-size: 64px;
    line-height: .8;
  }
  .blend-text { line-height: 1.05; transform: rotate(-4deg); padding-bottom: 6px; }
  .blend-text .lead { font-size: 20px; display: block; padding-left: 26px; }
  .blend-text .main { font-size: 30px; display: block; }
  .label--chicken .flavour,
  .label--chicken .product-line,
  .label--chicken .blend-count { color: var(--chicken); }
  .label--beef .flavour,
  .label--beef .blend-count { color: var(--beef); }
  .label--beef .product-line { color: var(--beef-soft); }
  .serving-photo {
    position: absolute;
    left: 0; right: 0; bottom: 0;
    height: 250px;
    background:
      radial-gradient(ellipse 120px 70px at 55% 52%, #fbfbf6 0%, #f3ecc4 55%, rgba(243,236,196,0) 100%),
      linear-gradient(180deg, var(--wood-light), var(--wood-dark));
  }
</style>
</head>
<body>
  <section class="label label--chicken">
    <div class="brand-tab">
      <span class="brand-dot"></span>
      <span class="brand-name">Verdant<br>Pressery</span>
      <span class="brand-tagline">Raw Organic Cold Pressed</span>
    </div>
    <h1 class="flavour">Chicken</h1>
    <p class="product-line">
      <svg width="40" height="8" viewBox="0 0 40 8"><line x1="0" y1="4" x2="34" y2="4" stroke="currentColor" stroke-width="2"/><circle cx="36" cy="4" r="3" fill="currentColor"/></svg>
      BONE BROTH
      <svg width="40" height="8" viewBox="0 0 40 8"><circle cx="4" cy="4" r="3" fill="currentColor"/><line x1="6" y1="4" x2="40" y2="4" stroke="currentColor" stroke-width="2"/></svg>
    </p>
    <p class="blend-note">
      <span class="blend-count">8</span>
      <span class="blend-text"><span class="lead">A blend of Ashwagandha and</span><span class="main">medicinal mushrooms</span></span>
    </p>
    <div class="serving-photo" role="img" aria-label="Bowl of golden bone broth with parsley and brown mushrooms on a light wooden table"></div>
  </section>

  <section class="label label--beef">
    <div class="brand-tab">
      <span class="brand-dot"></span>
      <span class="brand-name">Verdant<br>Pressery</span>
      <span class="brand-tagline">Raw Organic Cold Pressed</span>
    </div>
    <h1 class="flavour">Beef</h1>
    <p class="product-line">
      <svg width="40" height="8" viewBox="0 0 40 8"><line x1="0" y1="4" x2="34" y2="4" stroke="currentColor" stroke-width="2"/><circle cx="36" cy="4" r="3" fill="currentColor"/></svg>
      BONE BROTH
      <svg width="40" height="8" viewBox="0 0 40 8"><circle cx="4" cy="4" r="3" fill="currentColor"/><line x1="6" y1="4" x2="40" y2="4" stroke="currentColor" stroke-width="2"/></svg>
    </p>
    <p class="blend-note">
      <span class="blend-count">8</span>
      <span class="blend-text"><span class="lead">A blend of Ashwagandha and</span><span class="main">medicinal mushrooms</span></span>
    </p>
    <div class="serving-photo" role="img" aria-label="Bowl of golden bone broth with parsley and brown mushrooms on a light wooden table"></div>
  </section>
</body>
</html>
```